FLOUR BAG DESIGN

• Bag dimensions: H=280 mm, A=105 mm, B=65 mm (look at the picture »dimensions«)
• Bag will be used for different types of flour (wheat flour, corn flour, buckwheat flour, etc.) and porridge (buckwheat, millet, etc. ) so we are looking for universal design that will suit to all of them. Please have in mind that somewhere on the front side (AxH) there needs to be some space for the name of the flour/porridge.
• I also uploaded design of an existing bag just in case you want to see it. Design on the bag represents the mill where our business started. We could say that existing bag is very traditional, we are looking for a little bit more modern style bag but still want to emphasize the link to our tradition.

I forgot to select "10 days " when desribing the label desing I need, before posting the project

• • We would like to integrate our logo (look at the picture »logo«) and text which is also present on the current bag. Front side AxH: Koleškov Mlin (name of the company), Fužina – Zagradec (name of the village), Meljemo že od 1746 (meaning Flour milling since 1682). On the right side: same as on the picture »current bag (dimensions BxH)«.

```html
<!DOCTYPE html>
<html lang="sl">
<head>
<meta charset="utf-8">
<title>Koleškov Mlin – flour bag range</title>
<link href="https://fonts.googleapis.com/css2?family=Ubuntu:wght@400;500&family=Arimo:ital,wght@0,400;0,700;1,400&display=swap" rel="stylesheet">
<style>
  :root{
    --wheat:#7b4a1f;
    --wheat-dark:#5a3414;
    --corn:#4a5552;
    --corn-dark:#323b39;
    --buckwheat:#9a7a45;
    --buckwheat-dark:#6f5630;
    --millet:#4f6b3a;
    --millet-dark:#364a27;
    --brand-brown:#7a4a22;
    --paper:#ffffff;
    --sketch:#e6d2b6;
    --sketch-soft:#f7eee1;
  }
  *{box-sizing:border-box;margin:0;padding:0}
  html,body{width:1200px;height:800px;overflow:hidden;background:var(--paper)}
  .bag-range{display:flex;width:1200px;height:800px}
  .bag-front{
    position:relative;width:300px;height:800px;
    border-left:2px solid var(--brand-brown);
    border-right:1px solid var(--brand-brown);
    background:var(--paper);overflow:hidden;
  }
  .bag-front.wheat{--accent:var(--wheat);--accent-dark:var(--wheat-dark)}
  .bag-front.corn{--accent:var(--corn);--accent-dark:var(--corn-dark)}
  .bag-front.buckwheat{--accent:var(--buckwheat);--accent-dark:var(--buckwheat-dark)}
  .bag-front.millet{--accent:var(--millet);--accent-dark:var(--millet-dark)}

  .bag-art{position:absolute;inset:0;width:300px;height:800px}
  .accent-fill{fill:var(--accent)}
  .accent-dark-fill{fill:var(--accent-dark)}
  .accent-stroke{stroke:var(--accent);fill:none}
  .sun-glow{fill:url(#sunGlow)}

  .brand-name{
    position:absolute;top:166px;left:0;width:100%;text-align:center;
    font-family:"Ubuntu",sans-serif;font-weight:500;font-size:29px;
    color:var(--brand-brown);
  }
  .product-name{
    position:absolute;top:262px;left:40px;width:220px;text-align:center;
    font-family:"Arimo",sans-serif;font-weight:700;font-size:19px;
    color:#fff;letter-spacing:.5px;white-space:nowrap;
  }
  .product-name.long{font-size:17px;top:264px}
  .mill-illustration{
    position:absolute;top:300px;left:40px;width:220px;height:146px;
    border-radius:50%;
    background:radial-gradient(ellipse at 50% 45%,var(--sketch) 0%,var(--sketch-soft) 75%,var(--paper) 100%);
  }
  .tagline{
    position:absolute;top:452px;left:0;width:100%;text-align:center;
    font-family:"Ubuntu",sans-serif;font-size:22px;color:var(--brand-brown);
  }
  .contact{
    position:absolute;top:636px;left:0;width:100%;text-align:center;
    font-family:"Arimo",sans-serif;font-style:normal;color:var(--accent);
  }
  .contact .company{font-weight:700;font-size:17px;line-height:20px}
  .contact .owner,.contact .address{font-weight:700;font-size:12px;line-height:16px}
  .contact .phones{margin-top:12px;font-style:italic;font-size:12px;line-height:15px}
  .contact .web{margin-top:17px;font-style:italic;font-size:12px}
</style>
</head>
<body>
<svg width="0" height="0" style="position:absolute">
  <defs>
    <radialGradient id="sunGlow" cx="50%" cy="0%" r="90%">
      <stop offset="0%" stop-color="#fdd97a"/>
      <stop offset="45%" stop-color="#fff0c4"/>
      <stop offset="100%" stop-color="#ffffff"/>
    </radialGradient>
  </defs>
</svg>

<main class="bag-range">
  <section class="bag-front wheat">
    <svg class="bag-art" viewBox="0 0 300 800" aria-hidden="true">
      <path class="accent-dark-fill" d="M12,268 L44,268 L44,308 L12,308 L24,288 Z"/>
      <path class="accent-dark-fill" d="M288,268 L256,268 L256,308 L288,308 L276,288 Z"/>
      <path class="accent-fill" d="M38,258 Q150,252 262,258 L262,298 Q150,292 38,298 Z"/>
      <path class="accent-fill" d="M55,600 A95,95 0 0 1 245,600 L210,600 A60,60 0 0 0 90,600 Z"/>
      <path fill="#fff" d="M0,614 Q75,604 150,586 Q225,604 300,614 L300,800 L0,800 Z"/>
      <path class="sun-glow" role="img" aria-label="Sun rays rising over the mill" d="M0,620 Q75,610 150,592 Q225,610 300,620 L300,770 Q150,752 0,770 Z"/>
      <path class="accent-stroke" stroke-width="3" d="M0,612 Q75,602 150,584 Q225,602 300,612"/>
      <path class="accent-stroke" stroke-width="1.2" d="M0,622 Q75,612 150,594 Q225,612 300,622"/>
      <path class="accent-fill" d="M0,775 Q75,760 150,782 Q225,760 300,775 L300,800 L0,800 Z"/>
      <path class="accent-stroke" stroke-width="1.2" d="M0,767 Q75,752 150,774 Q225,752 300,767"/>
    </svg>
    <p class="brand-name">Koleškov mlin</p>
    <h2 class="product-name">WHEAT FLOUR</h2>
    <div class="mill-illustration" role="img" aria-label="Sketch of the old village mill buildings by the stream"></div>
    <p class="tagline">Meljemo že od 1746</p>
    <address class="contact">
      <div class="company">Koleškov Mlin</div>
      <div class="owner">Tomaž Kranjc s.p.</div>
      <div class="address">Brezje 14, 1310 Lipovec</div>
      <div class="phones">T: 01 555 20 40<br>M: 040 321 908</div>
      <div class="web">www.koleskov-mlin.si</div>
    </address>
  </section>

  <section class="bag-front corn">
    <svg class="bag-art" viewBox="0 0 300 800" aria-hidden="true">
      <path class="accent-dark-fill" d="M12,268 L44,268 L44,308 L12,308 L24,288 Z"/>
      <path class="accent-dark-fill" d="M288,268 L256,268 L256,308 L288,308 L276,288 Z"/>
      <path class="accent-fill" d="M38,258 Q150,252 262,258 L262,298 Q150,292 38,298 Z"/>
      <path class="accent-fill" d="M55,600 A95,95 0 0 1 245,600 L210,600 A60,60 0 0 0 90,600 Z"/>
      <path fill="#fff" d="M0,614 Q75,604 150,586 Q225,604 300,614 L300,800 L0,800 Z"/>
      <path class="sun-glow" role="img" aria-label="Sun rays rising over the mill" d="M0,620 Q75,610 150,592 Q225,610 300,620 L300,770 Q150,752 0,770 Z"/>
      <path class="accent-stroke" stroke-width="3" d="M0,612 Q75,602 150,584 Q225,602 300,612"/>
      <path class="accent-stroke" stroke-width="1.2" d="M0,622 Q75,612 150,594 Q225,612 300,622"/>
      <path class="accent-fill" d="M0,775 Q75,760 150,782 Q225,760 300,775 L300,800 L0,800 Z"/>
      <path class="accent-stroke" stroke-width="1.2" d="M0,767 Q75,752 150,774 Q225,752 300,767"/>
    </svg>
    <p class="brand-name">Koleškov mlin</p>
    <h2 class="product-name">CORN FLOUR</h2>
    <div class="mill-illustration" role="img" aria-label="Sketch of the old village mill buildings by the stream"></div>
    <p class="tagline">Meljemo že od 1746</p>
    <address class="contact">
      <div class="company">Koleškov Mlin</div>
      <div class="owner">Tomaž Kranjc s.p.</div>
      <div class="address">Brezje 14, 1310 Lipovec</div>
      <div class="phones">T: 01 555 20 40<br>M: 040 321 908</div>
      <div class="web">www.koleskov-mlin.si</div>
    </address>
  </section>

  <section class="bag-front buckwheat">
    <svg class="bag-art" viewBox="0 0 300 800" aria-hidden="true">
      <path class="accent-dark-fill" d="M12,268 L44,268 L44,308 L12,308 L24,288 Z"/>
      <path class="accent-dark-fill" d="M288,268 L256,268 L256,308 L288,308 L276,288 Z"/>
      <path class="accent-fill" d="M38,258 Q150,252 262,258 L262,298 Q150,292 38,298 Z"/>
      <path class="accent-fill" d="M55,600 A95,95 0 0 1 245,600 L210,600 A60,60 0 0 0 90,600 Z"/>
      <path fill="#fff" d="M0,614 Q75,604 150,586 Q225,604 300,614 L300,800 L0,800 Z"/>
      <path class="sun-glow" role="img" aria-label="Sun rays rising over the mill" d="M0,620 Q75,610 150,592 Q225,610 300,620 L300,770 Q150,752 0,770 Z"/>
      <path class="accent-stroke" stroke-width="3" d="M0,612 Q75,602 150,584 Q225,602 300,612"/>
      <path class="accent-stroke" stroke-width="1.2" d="M0,622 Q75,612 150,594 Q225,612 300,622"/>
      <path class="accent-fill" d="M0,775 Q75,760 150,782 Q225,760 300,775 L300,800 L0,800 Z"/>
      <path class="accent-stroke" stroke-width="1.2" d="M0,767 Q75,752 150,774 Q225,752 300,767"/>
    </svg>
    <p class="brand-name">Koleškov mlin</p>
    <h2 class="product-name long">BUCKWHEAT FLOUR</h2>
    <div class="mill-illustration" role="img" aria-label="Sketch of the old village mill buildings by the stream"></div>
    <p class="tagline">Meljemo že od 1746</p>
    <address class="contact">
      <div class="company">Koleškov Mlin</div>
      <div class="owner">Tomaž Kranjc s.p.</div>
      <div class="address">Brezje 14, 1310 Lipovec</div>
      <div class="phones">T: 01 555 20 40<br>M: 040 321 908</div>
      <div class="web">www.koleskov-mlin.si</div>
    </address>
  </section>

  <section class="bag-front millet">
    <svg class="bag-art" viewBox="0 0 300 800" aria-hidden="true">
      <path class="accent-dark-fill" d="M12,268 L44,268 L44,308 L12,308 L24,288 Z"/>
      <path class="accent-dark-fill" d="M288,268 L256,268 L256,308 L288,308 L276,288 Z"/>
      <path class="accent-fill" d="M38,258 Q150,252 262,258 L262,298 Q150,292 38,298 Z"/>
      <path class="accent-fill" d="M55,600 A95,95 0 0 1 245,600 L210,600 A60,60 0 0 0 90,600 Z"/>
      <path fill="#fff" d="M0,614 Q75,604 150,586 Q225,604 300,614 L300,800 L0,800 Z"/>
      <path class="sun-glow" role="img" aria-label="Sun rays rising over the mill" d="M0,620 Q75,610 150,592 Q225,610 300,620 L300,770 Q150,752 0,770 Z"/>
      <path class="accent-stroke" stroke-width="3" d="M0,612 Q75,602 150,584 Q225,602 300,612"/>
      <path class="accent-stroke" stroke-width="1.2" d="M0,622 Q75,612 150,594 Q225,612 300,622"/>
      <path class="accent-fill" d="M0,775 Q75,760 150,782 Q225,760 300,775 L300,800 L0,800 Z"/>
      <path class="accent-stroke" stroke-width="1.2" d="M0,767 Q75,752 150,774 Q225,752 300,767"/>
    </svg>
    <p class="brand-name">Koleškov mlin</p>
    <h2 class="product-name">MILLET PORRIDGE</h2>
    <div class="mill-illustration" role="img" aria-label="Sketch of the old village mill buildings by the stream"></div>
    <p class="tagline">Meljemo že od 1746</p>
    <address class="contact">
      <div class="company">Koleškov Mlin</div>
      <div class="owner">Tomaž Kranjc s.p.</div>
      <div class="address">Brezje 14, 1310 Lipovec</div>
      <div class="phones">T: 01 555 20 40<br>M: 040 321 908</div>
      <div class="web">www.koleskov-mlin.si</div>
    </address>
  </section>
</main>
</body>
</html>
```